Private Maths Tuition Flyer based in London

I am opening up a new Maths tuition centre in North West London. The flyer will be delivered to over 8,000 homes within the immediate vicinity. The design should be suitable to be printed on an A5 sheet and read in a portrait orientation.

The flyer should include the following:

The headline statement should be "Private Maths Tuition"

Secondary headline statement is the following "GCSE, A-Levels, 11 Plus exams"

Some of service offerings/selling points are:

- Free first session
- Monthly Feedback reports
- Free support outside of sessions
- Clear Target grades
- Personalised Lesson plans
- Tangible Results

Another statement that should be featured is "Book your free session by visiting www.lernova.co.uk" or something similar to that.

"Contact Details:
020 4719 8263
enquiries@lernova.co.uk"

"Address:
Kelbridge Business and Innovation Centre
Ashvale Court
Wrenfield Road
HA4 9QD"

Attached you'll see a logo which should be included and also a map of where we are. I am open to new images for the map if you guys have any, rather than a screen shot from google maps but it should be clear to see.

I would like the content above to be displayed in a clear and concise manner that is easy to read. You have creative license on where this information should be displayed and where the images should be but on the whole it should look aesthetically pleasing on the eye.

Target Market(s)

Students, Parents. Parents who want maths tutors.

Industry/Entity Type

Tutoring

Font styles to use
Sans Serif

Requirements
Must have
• *logo*
• Private Maths Tuition
• GCSE, A-Levels, 11 Plus exams
• - Free first session
• - Monthly Feedback reports
• - Free support outside of sessions
• - Clear Target grades
• - Personalised Lesson plans
• - Tangible Results
• Book your free session by visiting www.lernova.co.uk" or something similar to that.
• Contact Details:
• 020 4719 8263
• enquiries@lernova.co.uk
• Address (*with map*):
• Kelbridge Business and Innovation Centre
• Ashvale Court
• Wrenfield Road
• HA4 9QD
Nice to have
• similar colour scheme as the logo. creative background design.

```html
<!DOCTYPE html>
<html lang="en">
<head>
<meta charset="utf-8">
<title>Lernova – Private Maths Tuition Flyer</title>
<link href="https://fonts.googleapis.com/css2?family=Arimo:wght@400;700&display=swap" rel="stylesheet">
<style>
  :root{
    --backdrop:#2b2224;
    --paper:#ffffff;
    --green:#8cc63f;
    --blue:#0d4fa0;
    --navy:#123f8c;
    --orange:#ee6a1f;
    --ink:#1a1a1a;
    --map-base:#e4e2dc;
    --map-park:#c4dca2;
  }
  *{box-sizing:border-box;margin:0;padding:0}
  html,body{width:1200px;height:771px;overflow:hidden;background:var(--backdrop);font-family:"Arimo",Arial,sans-serif}
  .flyer{position:absolute;left:340px;top:18px;width:520px;height:735px;background:var(--paper);overflow:hidden;box-shadow:0 8px 30px rgba(0,0,0,.45)}
  .brand{position:absolute;top:26px;left:0;width:100%;display:flex;justify-content:center;align-items:center;gap:10px}
  .brand-mark{width:18px;height:18px;background:var(--green)}
  .brand-name{font-weight:700;font-size:40px;color:var(--orange);letter-spacing:.5px;line-height:48px}
  .headline-band{position:absolute;top:96px;left:0;width:100%;height:46px;background:var(--green)}
  .headline{position:absolute;top:104px;left:28px;font-weight:700;font-size:31px;line-height:32px;color:var(--paper);letter-spacing:.5px;text-transform:uppercase;white-space:nowrap}
  .subhead{position:absolute;top:156px;left:28px;font-weight:700;font-size:21px;line-height:26px;color:var(--orange);letter-spacing:.5px;white-space:nowrap}
  .offer-panel{position:absolute;top:196px;left:0;width:100%;height:152px;background:var(--blue)}
  .students-photo{position:absolute;top:196px;right:24px;width:190px;height:152px;background:linear-gradient(180deg,#d9c6a8 0%,#8a6f5a 45%,#2c2f3a 100%)}
  .offer-list{position:absolute;top:206px;left:26px;list-style:none}
  .offer-list li{position:relative;padding-left:26px;color:var(--paper);font-size:14.5px;line-height:22.5px;letter-spacing:.3px;white-space:nowrap}
  .offer-list li::before{content:"";position:absolute;left:2px;top:7px;width:9px;height:9px;background:var(--orange);transform:rotate(45deg)}
  .booking-band{position:absolute;top:348px;left:0;width:100%;height:44px;background:var(--orange)}
  .booking{position:absolute;top:360px;left:0;width:100%;text-align:center;font-weight:700;font-size:18px;line-height:20px;color:var(--paper);letter-spacing:.4px;white-space:nowrap}
  .location-map{position:absolute;top:414px;left:26px;width:240px;height:210px;background:linear-gradient(135deg,var(--map-base) 0%,var(--map-base) 55%,var(--map-park) 100%)}
  .contact{position:absolute;top:418px;left:282px;width:226px;color:var(--ink);font-size:11.5px;line-height:15px;font-style:normal;white-space:nowrap}
  .contact-title{font-weight:700;font-size:15px;line-height:18px;color:var(--navy);padding-bottom:3px;border-bottom:1px solid var(--green);display:inline-block;margin-bottom:8px}
  .contact-lines{margin-bottom:62px}
  .contact-direct p{margin-bottom:4px}
  .footer-band{position:absolute;bottom:0;left:0;width:100%;height:90px;background:var(--green)}
</style>
</head>
<body>
  <main class="flyer">
    <div class="brand">
      <span class="brand-mark"></span>
      <span class="brand-name">Lernova</span>
    </div>

    <div class="headline-band"></div>
    <h1 class="headline">Private Maths Tuition</h1>
    <h2 class="subhead">GCSE, A-Levels, 11 Plus exams</h2>

    <section class="offer-panel"></section>
    <div class="students-photo" role="img" aria-label="Two smiling students holding notebooks and wearing backpacks"></div>
    <ul class="offer-list">
      <li>Free first session</li>
      <li>Monthly Feedback reports</li>
      <li>Free support outside of sessions</li>
      <li>Clear Target grades</li>
      <li>Personalised Lesson plans</li>
      <li>Tangible Results</li>
    </ul>

    <div class="booking-band"></div>
    <p class="booking">Book your free session by visiting www.lernova.co.uk</p>

    <div class="location-map" role="img" aria-label="Street map showing the location of Kelbridge Business and Innovation Centre"></div>

    <address class="contact">
      <h3 class="contact-title">Contact us</h3>
      <div class="contact-lines">
        <p>Kelbridge Business and Innovation Centre</p>
        <p>Ashvale Court</p>
        <p>Wrenfield Road</p>
        <p>HA4 9QD</p>
      </div>
      <div class="contact-direct">
        <p>020 4719 8263</p>
        <p>enquiries@lernova.co.uk</p>
      </div>
    </address>

    <div class="footer-band"></div>
  </main>
</body>
</html>
```